Larkspur Ridge Management - Business Cards

I need business cards. My current logo was designed by a designer at this site and I very much like and am happy with the results. I would like a business card that is trendy, unique, current yet professional. I deal with high net worth clients daily

Target Market(s)

Out of state investors looking to get into the rental market in Ohio

Industry/Entity Type

Property Management, Consulting

Contact Information for Business Card

Name, Title (Chief Financial Officer) office phone number (555) 817-3094 website address larkridgemgmt.example

Font styles to use
Sans Serif

Colors
0054AA
0677BA
7BADD7
CADEEF
E8F1F8
0094D4
00A9DD
6FCCEA
C7EBF8
E9F6FB
00AB8E
00BBA5
67D7C9
C6EFE9
E9F9F6

```html
<!DOCTYPE html>
<html lang="en">
<head>
<meta charset="utf-8">
<title>Larkspur Ridge Management – Business Card</title>
<link rel="stylesheet" href="https://fonts.googleapis.com/css2?family=Montserrat:wght@600;700&family=Open+Sans:wght@400&display=swap">
<style>
  :root {
    --page-bg: #e9ecef;
    --card-bg: #242424;
    --card-edge: #c42a2a;
    --text-main: #ffffff;
    --text-soft: #e4e4e4;
    --mark-navy: #1f3566;
    --badge-grey: #8a8a8a;
  }
  * { margin: 0; padding: 0; box-sizing: border-box; }
  html, body {
    width: 1200px;
    height: 1000px;
    overflow: hidden;
    background: var(--page-bg);
  }
  .business-card {
    position: absolute;
    left: 75px;
    top: 200px;
    width: 1050px;
    height: 600px;
    background: var(--card-bg);
    border-left: 4px solid var(--card-edge);
    display: flex;
    align-items: center;
    box-shadow: 0 14px 40px rgba(0,0,0,0.18);
  }
  .brand-block {
    width: 500px;
    padding-left: 70px;
    display: flex;
    align-items: center;
    gap: 22px;
  }
  .brand-square {
    flex: none;
    width: 54px;
    height: 54px;
    background: var(--mark-navy);
  }
  .brand-name {
    font-family: "Montserrat", sans-serif;
    font-weight: 700;
    font-size: 40px;
    line-height: 1.15;
    color: var(--text-main);
    text-transform: uppercase;
    letter-spacing: 0.5px;
  }
  .contact-block {
    flex: 1;
    text-align: center;
    padding-right: 40px;
  }
  .person-name {
    font-family: "Montserrat", sans-serif;
    font-weight: 600;
    font-size: 46px;
    color: var(--text-main);
    letter-spacing: 1px;
    text-transform: uppercase;
  }
  .person-title {
    font-family: "Open Sans", sans-serif;
    font-size: 27px;
    color: var(--text-soft);
    margin-top: 6px;
  }
  .contact-list {
    list-style: none;
    margin-top: 64px;
    font-family: "Open Sans", sans-serif;
    font-size: 25px;
    line-height: 1.55;
    color: var(--text-soft);
  }
  .region-badge {
    display: block;
    margin: 40px auto 0;
  }
</style>
</head>
<body>
  <div class="business-card">
    <div class="brand-block">
      <span class="brand-square"></span>
      <span class="brand-name">Larkspur Ridge Management</span>
    </div>
    <div class="contact-block">
      <h1 class="person-name">Daniel Hartwell</h1>
      <p class="person-title">Chief Financial Officer</p>
      <ul class="contact-list">
        <li class="contact-phone">Office: (555) 817-3094</li>
        <li class="contact-web">larkridgemgmt.example</li>
        <li class="contact-email">daniel.hartwell@larkridgemgmt.example</li>
      </ul>
      <svg class="region-badge" width="90" height="90" viewBox="0 0 90 90" aria-hidden="true">
        <rect x="5" y="5" width="80" height="80" rx="4" fill="var(--badge-grey)"/>
      </svg>
    </div>
  </div>
</body>
</html>
```